Year End Gift for Employees

Looking for assistance in creating an album cover. Here are some ideas that I have: Double Platinum, Copper Lantern Drifting, 2025 World Tour
KT/RV (name of the band) – on the front of the album cover
List of Songs - on the back of the album cover
Would like to have the ability to have team / individual pictures on the inside of the double platinum album cover
DON’T want anything gory or vulgar for the album cover
Also want rights to the image for the album cover to use for t-shirts
This is a Sales Team that work within Brightwell Renovation Group
Any additional images that you want to propose, I'm open too. Thanks and I'll await your response
Colleagues

```html
<!DOCTYPE html>
<html lang="en">
<head>
<meta charset="utf-8">
<title>Copper Lantern Drifting – 2025 World Tour</title>
<link rel="stylesheet" href="https://fonts.googleapis.com/css2?family=Barlow:wght@400;600;700&family=IM+Fell+DW+Pica+SC&display=swap">
<style>
  :root {
    --stage: #d9d9db;
    --ink: #1b1b1c;
    --ink-soft: #2a2a2b;
    --paper: #f2f2f0;
    --spine: #8a8a8a;
    --rim: #e8e8e8;
  }
  * { box-sizing: border-box; margin: 0; padding: 0; }
  html, body { width: 1200px; height: 1000px; overflow: hidden; }
  body { background: var(--stage); position: relative; font-family: "Barlow", sans-serif; }

  .panel {
    position: absolute; top: 40px; width: 540px; height: 540px;
    background: var(--ink); color: var(--paper);
  }
  .panel--back { left: 50px; }
  .panel--front { left: 610px; }
  .spine { position: absolute; top: 40px; left: 590px; width: 20px; height: 540px; background: var(--spine); }

  .arc-title { position: absolute; inset: 0; width: 100%; height: 100%; z-index: 2; overflow: visible; }
  .arc-title text {
    font-family: "Barlow", sans-serif; font-weight: 700; fill: var(--paper); letter-spacing: 5px;
  }

  .emblem {
    position: absolute; z-index: 1;
    background: radial-gradient(ellipse at center, #9a9a9a 0%, #5a5a5a 35%, var(--ink-soft) 70%, transparent 100%);
    border-radius: 50%;
  }

  .band-name {
    position: absolute; left: 0; right: 0; text-align: center;
    font-family: "IM Fell DW Pica SC", serif; color: var(--paper); letter-spacing: 1px;
  }
  .band-code {
    position: absolute; left: 0; right: 0; text-align: center;
    font-family: "Barlow", sans-serif; font-weight: 700; letter-spacing: 3px; color: var(--paper);
  }

  .panel--front .emblem { left: 70px; top: 118px; width: 400px; height: 276px; }
  .panel--front .band-name { top: 405px; font-size: 33px; }
  .panel--front .band-code { top: 452px; font-size: 20px; }

  .panel--back .emblem { left: 140px; top: 110px; width: 260px; height: 180px; }
  .panel--back .band-name { top: 298px; font-size: 27px; }
  .tour-dates {
    position: absolute; top: 350px; left: 0; right: 0; list-style: none; text-align: center;
    font-size: 19px; letter-spacing: 2.5px; line-height: 31px; color: var(--paper);
  }

  .disc {
    position: absolute; left: 700px; top: 610px; width: 360px; height: 360px; border-radius: 50%;
    background: var(--ink); border: 6px solid var(--rim); overflow: hidden;
  }
  .disc .emblem { left: 64px; top: 36px; width: 220px; height: 175px; }
  .disc__hole {
    position: absolute; z-index: 2; left: 142px; top: 102px; width: 64px; height: 64px; border-radius: 50%;
    background: var(--stage); border: 10px solid #bdbdbd;
  }
  .disc .band-name { top: 232px; font-size: 21px; }
  .disc .band-code { top: 264px; font-size: 15px; }
</style>
</head>
<body>

  <section class="panel panel--back" aria-label="Tour dates panel">
    <div class="emblem" role="img" aria-label="Illustration: winged rearing horse on a shield with stars and a waving flag"></div>
    <svg class="arc-title" viewBox="0 0 540 540" aria-label="2025 World Tour">
      <defs><path id="arc-back" d="M 100 230 A 170 170 0 0 1 440 230"/></defs>
      <text font-size="30" text-anchor="middle"><textPath href="#arc-back" startOffset="50%">2025 WORLD TOUR</textPath></text>
    </svg>
    <h2 class="band-name">Copper Lantern Drifting</h2>
    <ul class="tour-dates">
      <li>1-5 DECEMBER • LAS VEGAS</li>
      <li>7-12 DECEMBER • LOS ANGELES</li>
      <li>14-18 DECEMBER • NEW YORK</li>
      <li>20-22 DECEMBER • CHICAGO</li>
      <li>24-25 DECEMBER • MIAMI</li>
    </ul>
  </section>

  <div class="spine"></div>

  <section class="panel panel--front" aria-label="Front cover">
    <div class="emblem" role="img" aria-label="Illustration: winged rearing horse on a shield with stars and a waving flag"></div>
    <svg class="arc-title" viewBox="0 0 540 540" aria-label="2025 World Tour">
      <defs><path id="arc-front" d="M 50 300 A 220 220 0 0 1 490 300"/></defs>
      <text font-size="34" text-anchor="middle"><textPath href="#arc-front" startOffset="50%">2025 WORLD TOUR</textPath></text>
    </svg>
    <h1 class="band-name">Copper Lantern Drifting</h1>
    <p class="band-code">KT/RV</p>
  </section>

  <section class="disc" aria-label="Disc">
    <div class="emblem" role="img" aria-label="Illustration: winged rearing horse on a shield"></div>
    <div class="disc__hole"></div>
    <p class="band-name">Copper Lantern Drifting</p>
    <p class="band-code">KT/RV</p>
  </section>

</body>
</html>
```